2022 Landscaping Services

Please use the prior year design as an example. Similar style but DO NOT COPY IT EXACTLY- you can use different photos from our website if you like. Same text for year 2022.
Design should clearly depict the differences between the 3 products so people can buy one of them. Be creative!

size 8.5" x 11"

Must provide source file in photoshop if you are winner

Requirements
Must have
• Same text as original flier but with year 2022

```html
<!DOCTYPE html>
<html lang="en">
<head>
<meta charset="utf-8">
<title>2022 Gravesite Landscaping Package</title>
<link href="https://fonts.googleapis.com/css2?family=Montserrat:wght@400;500;600;700&family=Lobster&display=swap" rel="stylesheet">
<style>
  :root {
    --maroon: #7a2331;
    --navy: #1e2a44;
    --grey: #d6d2d2;
    --white: #ffffff;
    --photo-dark: #4f5a3a;
    --photo-gold: #c9a441;
  }
  * { margin: 0; padding: 0; box-sizing: border-box; }
  html, body { width: 927px; height: 1200px; overflow: hidden; background: var(--white); }
  body { font-family: "Montserrat", sans-serif; }
  .flyer { position: relative; width: 927px; height: 1200px; overflow: hidden; background: var(--white); }

  .hero-photo {
    position: absolute; left: 0; top: 0; width: 927px; height: 460px;
    background: linear-gradient(160deg, #8a7a3a 0%, var(--photo-gold) 30%, #e8d9a0 55%, #8d9078 70%, var(--photo-dark) 100%);
  }
  .hero-band { position: absolute; left: 0; top: 0; width: 927px; height: 570px; }

  .brand {
    position: absolute; left: 0; top: 50px; width: 303px; height: 73px;
    background: var(--white); display: flex; align-items: center; justify-content: center; gap: 10px;
    color: var(--maroon); font-weight: 600; font-size: 17px; letter-spacing: 0.5px;
  }
  .brand-dot { width: 14px; height: 14px; border-radius: 50%; background: var(--maroon); }

  .title { position: absolute; right: 29px; color: var(--white); font-weight: 600; text-align: right; line-height: 1; }
  .title-year { top: 352px; font-size: 70px; }
  .title-line1 { top: 427px; font-size: 46px; }
  .title-line2 { top: 484px; font-size: 46px; }

  .services-heading {
    position: absolute; left: 26px; top: 577px; color: var(--maroon);
    font-weight: 700; font-size: 27px; line-height: 27px;
  }
  .service {
    position: absolute; left: 26px; color: var(--navy); font-weight: 500;
    font-size: 13px; line-height: 18px; letter-spacing: 0.4px;
  }
  .validity { position: absolute; left: 26px; top: 1018px; color: var(--navy); font-weight: 500; font-size: 19px; line-height: 25px; }

  .plan { position: absolute; text-align: center; }
  .plan-head { height: 65px; display: flex; flex-direction: column; justify-content: center; line-height: 1.15; }
  .plan-name { font-size: 19px; font-weight: 500; letter-spacing: 0.5px; }
  .plan-sub { font-size: 14px; font-weight: 500; letter-spacing: 0.3px; }
  .plan-body { position: relative; }
  .plan-freq { font-size: 10.5px; line-height: 14px; padding-top: 17px; font-weight: 500; }

  .plan-seasonal { left: 244px; top: 569px; width: 205px; }
  .plan-seasonal .plan-head, .plan-basic .plan-head { background: var(--grey); color: var(--navy); }
  .plan-seasonal .plan-body, .plan-basic .plan-body { background: var(--maroon); color: var(--white); height: 459px; }

  .plan-perpetual { left: 450px; top: 550px; width: 249px; box-shadow: 0 3px 8px rgba(0,0,0,0.25); z-index: 2; }
  .plan-perpetual .plan-head { background: var(--maroon); color: var(--white); height: 84px; padding-top: 6px; }
  .plan-perpetual .plan-body { background: var(--white); color: var(--maroon); height: 486px; }
  .plan-perpetual .plan-freq { padding-top: 20px; }

  .plan-basic { left: 699px; top: 569px; width: 205px; }

  .mark { position: absolute; left: 50%; width: 24px; height: 24px; margin-left: -12px; }

  .rule { position: absolute; left: 16px; right: 16px; height: 1.5px; background: var(--white); }
  .plan-perpetual .rule { left: 33px; right: 33px; height: 3px; background: var(--maroon); }

  .price-row { position: absolute; left: 16px; right: 16px; top: 437px; display: flex; justify-content: space-between; }
  .price-cell { flex: 1; line-height: 1; }
  .price-cell + .price-cell { border-left: 1px solid var(--white); }
  .price-small { font-size: 19px; font-weight: 600; }
  .price-term { font-size: 8.5px; margin-top: 4px; }
  .price-note { position: absolute; left: 0; right: 0; font-size: 9.5px; line-height: 13px; }
  .price-big { position: absolute; left: 0; right: 0; font-weight: 600; line-height: 1; }

  .popular-badge {
    position: absolute; left: 666px; top: 535px; width: 58px; height: 58px; border-radius: 50%;
    background: var(--white); box-shadow: 0 1px 4px rgba(0,0,0,0.3); z-index: 3;
    display: flex; align-items: center; justify-content: center; text-align: center;
    font-family: "Lobster", cursive; color: var(--maroon); font-size: 12px; line-height: 13px;
    transform: rotate(-6deg);
  }

  .footer-bar {
    position: absolute; left: 0; top: 1150px; width: 452px; height: 50px; background: var(--maroon);
    color: var(--white); font-size: 15.5px; font-weight: 500; padding-left: 33px; line-height: 50px;
  }
  .footer-contact {
    position: absolute; left: 452px; top: 1158px; width: 475px; text-align: center;
    color: var(--maroon); font-size: 15.5px; font-weight: 500;
  }
  .footer-line { position: absolute; left: 452px; right: 0; top: 1183px; height: 2px; background: var(--maroon); }
</style>
</head>
<body>
<svg width="0" height="0" style="position:absolute">
  <defs>
    <symbol id="icon-yes" viewBox="0 0 24 24">
      <circle cx="12" cy="12" r="10.5" fill="none" stroke="currentColor" stroke-width="2"/>
      <path d="M7 12.5 L10.5 16 L17 8.5" fill="none" stroke="currentColor" stroke-width="2.2" stroke-linecap="round" stroke-linejoin="round"/>
    </symbol>
    <symbol id="icon-no" viewBox="0 0 24 24">
      <circle cx="12" cy="12" r="10.5" fill="none" stroke="currentColor" stroke-width="2"/>
      <path d="M8.5 8.5 L15.5 15.5 M15.5 8.5 L8.5 15.5" fill="none" stroke="currentColor" stroke-width="2.2" stroke-linecap="round"/>
    </symbol>
  </defs>
</svg>

<main class="flyer">
  <div class="hero-photo" role="img" aria-label="Photo of a cemetery with rows of headstones under autumn trees, sun shining through golden leaves"></div>
  <svg class="hero-band" viewBox="0 0 927 570" aria-hidden="true">
    <polygon points="0,437 927,305 927,570 0,570" fill="var(--maroon)"/>
  </svg>

  <div class="brand"><span class="brand-dot"></span>Willowbrook Cemetery</div>

  <h1>
    <span class="title title-year">2022</span>
    <span class="title title-line1">GRAVESITE</span>
    <span class="title title-line2">LANDSCAPING PACKAGE</span>
  </h1>

  <h2 class="services-heading">SERVICES<br>OFFERED</h2>
  <p class="service" style="top:653px">WEDDING &amp; TRIMMING ON<br>YOUR GRAVESITE</p>
  <p class="service" style="top:703px">PAYMENT ENSURED<br>FOREVER GRAVE CAR</p>
  <p class="service" style="top:752px">WEDDING &amp; TRIMMING ON<br>YOUR GRAVESITE</p>
  <p class="service" style="top:802px">PAYMENT ENSURED<br>FOREVER GRAVE CAR</p>
  <p class="service" style="top:851px">PAYMENT ENSURED<br>FOREVER GRAVE CAR</p>
  <p class="service" style="top:901px">WEDDING &amp; TRIMMING ON<br>YOUR GRAVESITE</p>
  <p class="service" style="top:950px">PAYMENT ENSURED<br>FOREVER GRAVE CAR</p>
  <p class="validity">Valid through<br>10/31/22</p>

  <section class="plan plan-seasonal">
    <div class="plan-head"><span class="plan-name">SEASONAL</span><span class="plan-sub">CARE ENDOWMENT</span></div>
    <div class="plan-body">
      <p class="plan-freq">Approximately every 7 weeks<br>during the growing season:<br>Mid-April through Mid-October</p>
      <svg class="mark" style="top:77px;color:var(--white)"><use href="#icon-yes"/></svg>
      <svg class="mark" style="top:129px;color:var(--white)"><use href="#icon-no"/></svg>
      <svg class="mark" style="top:178px;color:var(--white)"><use href="#icon-no"/></svg>
      <svg class="mark" style="top:228px;color:var(--white)"><use href="#icon-no"/></svg>
      <svg class="mark" style="top:277px;color:var(--white)"><use href="#icon-no"/></svg>
      <svg class="mark" style="top:327px;color:var(--white)"><use href="#icon-no"/></svg>
      <div class="rule" style="top:361px"></div>
      <div class="price-row" style="top:377px">
        <div class="price-cell"><div class="price-small">$357</div><div class="price-term">3 Years</div></div>
        <div class="price-cell"><div class="price-small">$238</div><div class="price-term">2 Years</div></div>
        <div class="price-cell"><div class="price-small">$119</div><div class="price-term">1 Years</div></div>
      </div>
      <p class="price-note" style="top:426px">Multi-year payment locks<br>in current rates.</p>
    </div>
  </section>

  <div class="popular-badge">Most<br>Popular</div>

  <section class="plan plan-perpetual">
    <div class="plan-head"><span class="plan-name">PERPETUAL</span><span class="plan-sub">CARE ENDOWMENT</span></div>
    <div class="plan-body">
      <p class="plan-freq">Approximately every 7 weeks<br>during the growing season:<br>Mid-April through Mid-October</p>
      <svg class="mark" style="top:84px;color:var(--maroon)"><use href="#icon-yes"/></svg>
      <svg class="mark" style="top:139px;color:var(--maroon)"><use href="#icon-yes"/></svg>
      <svg class="mark" style="top:192px;color:var(--maroon)"><use href="#icon-yes"/></svg>
      <svg class="mark" style="top:246px;color:var(--maroon)"><use href="#icon-yes"/></svg>
      <svg class="mark" style="top:298px;color:var(--maroon)"><use href="#icon-yes"/></svg>
      <svg class="mark" style="top:352px;color:var(--maroon)"><use href="#icon-yes"/></svg>
      <div class="rule" style="top:388px"></div>
      <div class="price-big" style="top:402px;font-size:31px">$313</div>
      <p class="price-note" style="top:436px;font-size:10.5px;line-height:15px">12 Monthly payments.<br>Call for single payment<br>discount.</p>
    </div>
  </section>

  <section class="plan plan-basic">
    <div class="plan-head"><span class="plan-name">BASIC</span><span class="plan-sub">CARE ENDOWMENT</span></div>
    <div class="plan-body">
      <p class="plan-freq">2 times per year:<br>Mid-May &amp; Mid-September</p>
      <svg class="mark" style="top:77px;color:var(--white)"><use href="#icon-yes"/></svg>
      <svg class="mark" style="top:129px;color:var(--white)"><use href="#icon-yes"/></svg>
      <svg class="mark" style="top:178px;color:var(--white)"><use href="#icon-no"/></svg>
      <svg class="mark" style="top:228px;color:var(--white)"><use href="#icon-no"/></svg>
      <svg class="mark" style="top:277px;color:var(--white)"><use href="#icon-no"/></svg>
      <svg class="mark" style="top:327px;color:var(--white)"><use href="#icon-no"/></svg>
      <div class="rule" style="top:361px"></div>
      <div class="price-big" style="top:374px;font-size:29px">$255</div>
      <p class="price-note" style="top:407px;font-size:10px">12 Monthly payments.<br>Call for single payment<br>discount.</p>
    </div>
  </section>

  <footer>
    <div class="footer-bar">48 Orchard Ln. Fairview NJ 07022</div>
    <div class="footer-contact">(201) 555-0148 &nbsp;|&nbsp; willowbrookcemetery.org</div>
    <div class="footer-line"></div>
  </footer>
</main>
</body>
</html>
```